Business card for auto dealership

Looking for a clean modern design.
Would like attached logo incorporated

Industry/Entity Type

Car dealership

Contact Information for Business Card

Name, website, phone, cell, fax, email

```html
<!DOCTYPE html>
<html lang="en">
<head>
<meta charset="utf-8">
<title>Halvorsen Truck &amp; Auto Sales – Business Card</title>
<link rel="stylesheet" href="https://fonts.googleapis.com/css2?family=Montserrat:wght@300;500;600&family=Open+Sans:wght@500;600&display=swap">
<style>
  :root {
    --bg: #2a2e35;
    --card-white: #ffffff;
    --brand-red: #8b1619;
    --ink: #1e1e1e;
    --muted: #6d6d6d;
    --rule: #9a2a2b;
  }
  * { box-sizing: border-box; margin: 0; padding: 0; }
  html, body { width: 1200px; height: 780px; overflow: hidden; }
  body { background: var(--bg); position: relative; font-family: "Open Sans", sans-serif; }

  .card { position: absolute; border-radius: 22px; box-shadow: 0 10px 30px rgba(0,0,0,.35); }

  /* Front side */
  .card-front {
    left: 150px; top: 105px; width: 330px; height: 570px;
    background: var(--card-white);
    padding: 64px 24px 0;
    display: flex; flex-direction: column; align-items: center;
    color: var(--ink);
  }
  .wordmark { text-align: center; font-family: "Montserrat", sans-serif; font-weight: 600; line-height: 1; }
  .wordmark-name { display: block; font-size: 40px; letter-spacing: -.5px; }
  .wordmark-tag { display: block; font-size: 12px; letter-spacing: 1.5px; margin-top: 6px; }
  .front-wordmark { color: var(--ink); }

  .person { margin-top: 40px; align-self: stretch; text-align: center; font-family: "Montserrat", sans-serif; }
  .person-name { font-size: 29px; font-weight: 600; letter-spacing: .3px; white-space: nowrap; }
  .person-surname { color: var(--brand-red); }
  .person-title { font-size: 12px; font-weight: 300; letter-spacing: 1px; color: var(--muted); margin-top: 4px; padding-left: 110px; }

  .divider { align-self: stretch; display: flex; align-items: center; gap: 8px; margin-top: 22px; }
  .divider-rule { flex: 1; height: 1px; background: var(--rule); }
  .icon-set { display: flex; gap: 5px; }
  .icon { width: 20px; height: 20px; border-radius: 5px; background: var(--brand-red); display: flex; align-items: center; justify-content: center; }
  .icon svg { width: 13px; height: 13px; fill: none; stroke: #fff; stroke-width: 1.8; stroke-linecap: round; stroke-linejoin: round; }

  .contact-list { list-style: none; text-align: center; margin-top: 10px; font-size: 15.5px; font-weight: 600; line-height: 1.45; color: var(--ink); }

  /* Back side */
  .card-back {
    left: 545px; top: 225px; width: 570px; height: 330px;
    background: var(--brand-red);
    display: flex; align-items: center; justify-content: center;
  }
  .back-wordmark { color: #fff; }
  .back-wordmark .wordmark-name { font-size: 72px; letter-spacing: -1px; }
  .back-wordmark .wordmark-tag { font-size: 19px; letter-spacing: 3px; margin-top: 10px; }
</style>
</head>
<body>

<section class="card card-front" aria-label="Business card front">
  <div class="wordmark front-wordmark">
    <span class="wordmark-name">Halvorsen</span>
    <span class="wordmark-tag">TRUCK &amp; AUTO SALES</span>
  </div>

  <div class="person">
    <p class="person-name">Dana <span class="person-surname">Halvorsen</span></p>
    <p class="person-title">FOUNDER/CEO</p>
  </div>

  <div class="divider">
    <span class="divider-rule"></span>
    <div class="icon-set">
      <span class="icon" aria-label="Cell"><svg viewBox="0 0 16 16"><rect x="4.5" y="1.5" width="7" height="13" rx="1.5"/><path d="M7 12h2"/></svg></span>
      <span class="icon" aria-label="Email"><svg viewBox="0 0 16 16"><rect x="1.5" y="3.5" width="13" height="9" rx="1"/><path d="M2 4l6 5 6-5"/></svg></span>
      <span class="icon" aria-label="Website"><svg viewBox="0 0 16 16"><circle cx="8" cy="8" r="6"/><path d="M2 8h12M8 2c2 2 2 10 0 12M8 2c-2 2-2 10 0 12"/></svg></span>
    </div>
    <span class="divider-rule"></span>
  </div>

  <ul class="contact-list">
    <li>555-240-9371</li>
    <li>dana@halvorsenauto.com</li>
    <li>www.halvorsenauto.com</li>
  </ul>

  <div class="divider">
    <span class="divider-rule"></span>
    <div class="icon-set">
      <span class="icon" aria-label="Phone"><svg viewBox="0 0 16 16"><path d="M3 5.5c0-2 1-3 3-3l1 2.5-1.5 1c.6 1.6 1.9 2.9 3.5 3.5l1-1.5L13 9c0 2-1 3-3 3C6 12 3 9 3 5.5z"/></svg></span>
      <span class="icon" aria-label="Fax"><svg viewBox="0 0 16 16"><rect x="2" y="6" width="12" height="6" rx="1"/><path d="M4.5 6V2h7v4M4.5 12v2h7v-2"/></svg></span>
    </div>
    <span class="divider-rule"></span>
  </div>

  <ul class="contact-list">
    <li>555-406-2958</li>
    <li>555-317-6842</li>
  </ul>
</section>

<section class="card card-back" aria-label="Business card back">
  <div class="wordmark back-wordmark">
    <span class="wordmark-name">Halvorsen</span>
    <span class="wordmark-tag">TRUCK &amp; AUTO SALES</span>
  </div>
</section>

</body>
</html>
```